Harbourlight Geriatric care need Business card design

Simple and elegance looking business card (colour choice will be very important)
Harbourlight geriatric care is medical consultation service for elderly population.

1st side---business logo and the doctor name/tile
eg: dr. XXX
MBBS,FRACP etc
Main room:
suite xxx AAA medical centre 18 XXX road Vic 3000
Phone:
Fax:

2nd side --different clinic address (up to 3 addresses) and need to have appointment time/ date

Suite xxx AAA medical centre , 18 XXX road VIC 3000

Please see attachment for business logo

Important: need to be compatible with Quillo Press for printing purpose.

Thank you.

hi, please look at the sample business card and create something similar. Company name: Harbourlight Geriatric Care PTY LTD ABN 47580916 ( all small font and no need to be obvious) company logo need to be obvious Apart from steadfast in support, also add Geriatrician for Community and Residential Care. Main room Pondaro Medical Centre suite 2.07 204-206 Larkspur street Box Hill Vic All appointment and enquiries: tel: 908716252 Fasmile: www.qwvplmzk.com.au Tindlewood Medical Centre 42 gorrington road mooroolbark VIC Bayview Crest Private Frankston 87 Pellworth road , franskton VIC 3199 Oakrun Private Hospital specialist room 259 Dunmore Road, Mt. Waverley VIC 3333 Dr. TM 81920kp DR. RH w7169208nd DR. PJ 670918vt Thank you

```html
<!DOCTYPE html>
<html lang="en">
<head>
<meta charset="utf-8">
<title>Harbourlight Geriatric Care — Business Card</title>
<link rel="stylesheet" href="https://fonts.googleapis.com/css2?family=Arimo:wght@400;700&family=Crimson+Pro:wght@500&family=Noto+Serif:wght@700&display=swap">
<style>
  :root {
    --bg: #e9e6e1;
    --card-white: #f7f7f7;
    --navy: #26398c;
    --navy-deep: #1f2f7a;
    --red: #d8263a;
    --ink-grey: #8d8f96;
    --line: #2b2b2b;
    --text-light: #ffffff;
  }
  * { box-sizing: border-box; margin: 0; padding: 0; }
  html, body { width: 1200px; height: 885px; overflow: hidden; }
  body {
    background: var(--bg);
    font-family: "Arimo", Arial, sans-serif;
    display: flex;
    align-items: center;
    justify-content: center;
    gap: 50px;
  }
  .card {
    width: 520px;
    height: 300px;
    border-radius: 14px;
    overflow: hidden;
    background: var(--card-white);
    box-shadow: 0 6px 18px rgba(0,0,0,0.18);
    position: relative;
  }

  /* Front */
  .front { display: flex; flex-direction: column; }
  .front__brand {
    height: 132px;
    padding: 30px 30px 0 30px;
    display: flex;
    flex-direction: column;
  }
  .brand-name {
    display: flex;
    align-items: center;
    gap: 12px;
    font-family: "Crimson Pro", Georgia, serif;
    font-weight: 500;
    font-size: 40px;
    color: var(--navy);
    line-height: 1;
    white-space: nowrap;
  }
  .brand-dot {
    width: 30px; height: 30px;
    border-radius: 50%;
    background: var(--red);
    flex: none;
  }
  .brand-tagline {
    margin: 8px 0 0 100px;
    font-size: 13px;
    letter-spacing: 6px;
    text-transform: uppercase;
    color: var(--ink-grey);
  }
  .front__band {
    height: 36px;
    background: var(--red);
    color: var(--text-light);
    display: flex;
    align-items: center;
    padding-left: 132px;
    gap: 6px;
  }
  .employee-name {
    font-family: "Noto Serif", Georgia, serif;
    font-weight: 700;
    font-size: 18px;
  }
  .employee-title {
    font-size: 13px;
    border-left: 1px solid rgba(255,255,255,0.8);
    padding-left: 5px;
  }
  .front__contact {
    flex: 1;
    background: var(--navy);
    color: var(--text-light);
    padding: 22px 0 0 200px;
    font-size: 17px;
    line-height: 1.3;
  }
  .contact-line--indent { padding-left: 20px; }

  /* Back */
  .back { padding: 34px 32px; color: var(--navy-deep); font-size: 16px; }
  .appointment-label { color: var(--line); font-size: 15px; margin-bottom: 4px; }
  .appointment-row {
    display: flex;
    align-items: flex-end;
    gap: 10px;
    color: var(--line);
    font-size: 15px;
    margin-bottom: 30px;
  }
  .appointment-field { display: flex; align-items: flex-end; gap: 6px; }
  .appointment-field--date { flex: 1.25; }
  .appointment-field--time { flex: 1; }
  .write-line { flex: 1; border-bottom: 1px solid var(--line); height: 18px; }
  .clinic-list { list-style: none; }
  .clinic-list li { margin-bottom: 14px; }
</style>
</head>
<body>
  <section class="card front" aria-label="Business card front">
    <div class="front__brand">
      <div class="brand-name"><span class="brand-dot"></span>Harbourlight Geriatric Care</div>
      <div class="brand-tagline">steadfast in support</div>
    </div>
    <div class="front__band">
      <span class="employee-name">Employee Name</span>
      <span class="employee-title">MBBS,FRACP</span>
    </div>
    <div class="front__contact">
      <div class="contact-line">P xxxx xxx xxx</div>
      <div class="contact-line">F xxxx xxx xxx</div>
      <div class="contact-line">suite xxx AAA medical centre</div>
      <div class="contact-line contact-line--indent">18 XXX road Vic 3000</div>
    </div>
  </section>

  <section class="card back" aria-label="Business card back">
    <div class="appointment-label">Appointment</div>
    <div class="appointment-row">
      <div class="appointment-field appointment-field--date"><span>Date:</span><span class="write-line"></span></div>
      <div class="appointment-field appointment-field--time"><span>Time:</span><span class="write-line"></span></div>
    </div>
    <ul class="clinic-list">
      <li>Suite xxx AAA medical centre , 18 XXX road VIC 3000</li>
      <li>Suite xxx AAA medical centre , 18 XXX road VIC 3000</li>
      <li>Suite xxx AAA medical centre , 18 XXX road VIC 3000</li>
    </ul>
  </section>
</body>
</html>
```